Design of two graphics from basic existing design & colours

I have two graphics which I currently use but they are nothing special. We would like to transform these two graphics, using our existing logo colour, into something special. The outputs will be used:

- on our website;
- in a powerpoint sales presentation;
- in email campaigns; and
- to print for handing to prospects at the end of a sales presentation.

Please just submit one of the graphics and if we like the design, we will ask you to work on the second graphic. These two graphics are critical to our marketing and will be used together so we need them to have a similar look and feel.

```html
<!DOCTYPE html>
<html lang="en">
<head>
<meta charset="utf-8">
<title>Advisory Board – Managing Structure &amp; Performance</title>
<link rel="stylesheet" href="https://fonts.googleapis.com/css2?family=Open+Sans:wght@400&display=swap">
<style>
  :root {
    --red: #d62e2e;
    --black: #1a1a1a;
    --charcoal: #3d3a3b;
    --grey: #a0a0a0;
    --grey-text: #a6a6a6;
    --maroon: #6b1f1f;
    --paper: #ffffff;
  }
  html, body {
    margin: 0;
    padding: 0;
    width: 1200px;
    height: 980px;
    overflow: hidden;
    background: var(--paper);
  }
  .cycle-diagram {
    display: block;
    width: 1200px;
    height: 980px;
    font-family: "Open Sans", Arial, sans-serif;
  }
  .segment--red { fill: var(--red); }
  .segment--black { fill: var(--black); }
  .segment--charcoal { fill: var(--charcoal); }
  .segment--grey { fill: var(--grey); }
  .flow-arrow { fill: none; stroke: var(--paper); stroke-width: 8; stroke-linecap: butt; }
  .spoke { fill: none; stroke-width: 24; }
  .spoke--red { stroke: var(--red); }
  .spoke--black { stroke: var(--black); }
  .spoke--charcoal { stroke: var(--charcoal); }
  .spoke--grey { stroke: var(--grey); }
  .node-box { fill: var(--paper); stroke-width: 2.5; }
  .node--red .node-box { stroke: var(--red); }
  .node--red .node-label { fill: var(--red); }
  .node--black .node-box { stroke: var(--black); }
  .node--black .node-label { fill: var(--black); }
  .node--charcoal .node-box { stroke: var(--charcoal); }
  .node--charcoal .node-label { fill: var(--charcoal); }
  .node--grey .node-box { stroke: var(--grey-text); }
  .node--grey .node-label { fill: var(--grey-text); }
  .node-label { font-size: 28px; text-anchor: middle; }
  .hub-caption { fill: var(--maroon); font-size: 21px; text-anchor: middle; }
  .hub-title { fill: var(--maroon); font-size: 26px; text-anchor: middle; }
  .hub-divider { stroke: var(--maroon); stroke-width: 2; }
</style>
</head>
<body>
<svg class="cycle-diagram" viewBox="0 0 1470 1220" preserveAspectRatio="xMidYMid meet" role="img" aria-label="Advisory Board cycle: managing structure and managing performance">
  <defs>
    <marker id="head-red" viewBox="0 0 10 10" refX="1" refY="5" markerUnits="userSpaceOnUse" markerWidth="52" markerHeight="58" orient="auto"><path d="M0 0 L10 5 L0 10 Z" fill="#d62e2e"/></marker>
    <marker id="head-black" viewBox="0 0 10 10" refX="1" refY="5" markerUnits="userSpaceOnUse" markerWidth="52" markerHeight="58" orient="auto"><path d="M0 0 L10 5 L0 10 Z" fill="#1a1a1a"/></marker>
    <marker id="head-charcoal" viewBox="0 0 10 10" refX="1" refY="5" markerUnits="userSpaceOnUse" markerWidth="52" markerHeight="58" orient="auto"><path d="M0 0 L10 5 L0 10 Z" fill="#3d3a3b"/></marker>
    <marker id="head-grey" viewBox="0 0 10 10" refX="1" refY="5" markerUnits="userSpaceOnUse" markerWidth="52" markerHeight="58" orient="auto"><path d="M0 0 L10 5 L0 10 Z" fill="#a0a0a0"/></marker>
    <marker id="head-white" viewBox="0 0 10 10" refX="1" refY="5" markerUnits="userSpaceOnUse" markerWidth="20" markerHeight="22" orient="auto"><path d="M0 0 L10 5 L0 10 Z" fill="#ffffff"/></marker>
    <g id="ring-segment">
      <path d="M693.3 378.5 A250 250 0 0 1 822.7 378.5 L790.4 499.3 A125 125 0 0 0 725.6 499.3 Z"/>
      <path class="flow-arrow" d="M731.8 433.8 A188 188 0 0 1 770 432.5" marker-end="url(#head-white)"/>
    </g>
  </defs>

  <!-- spokes -->
  <path class="spoke spoke--red" d="M754 360 C754 320 735 305 728 292" marker-end="url(#head-red)"/>
  <path class="spoke spoke--black" d="M890 432 C915 410 925 390 930 360" marker-end="url(#head-black)"/>
  <path class="spoke spoke--grey" d="M1005 530 C1040 520 1050 505 1065 492" marker-end="url(#head-grey)"/>
  <path class="spoke spoke--red" d="M978 700 C1010 708 1030 708 1055 705" marker-end="url(#head-red)"/>
  <path class="spoke spoke--charcoal" d="M912 840 C935 870 955 880 980 890" marker-end="url(#head-charcoal)"/>
  <path class="spoke spoke--red" d="M762 868 C762 900 765 915 775 935" marker-end="url(#head-red)"/>
  <path class="spoke spoke--black" d="M604 842 C585 870 575 890 570 912" marker-end="url(#head-black)"/>
  <path class="spoke spoke--grey" d="M530 695 C500 705 485 715 465 735" marker-end="url(#head-grey)"/>
  <path class="spoke spoke--red" d="M505 550 C480 540 460 536 432 538" marker-end="url(#head-red)"/>
  <path class="spoke spoke--charcoal" d="M602 440 C585 415 570 405 548 392" marker-end="url(#head-charcoal)"/>

  <!-- ring -->
  <g class="ring">
    <use href="#ring-segment" class="segment--red" transform="translate(0 -6) rotate(0 758 620)"/>
    <use href="#ring-segment" class="segment--black" transform="translate(0 -6) rotate(36 758 620)"/>
    <use href="#ring-segment" class="segment--grey" transform="translate(0 -6) rotate(72 758 620)"/>
    <use href="#ring-segment" class="segment--red" transform="translate(0 6) rotate(108 758 620)"/>
    <use href="#ring-segment" class="segment--charcoal" transform="translate(0 6) rotate(144 758 620)"/>
    <use href="#ring-segment" class="segment--red" transform="translate(0 6) rotate(180 758 620)"/>
    <use href="#ring-segment" class="segment--black" transform="translate(0 6) rotate(216 758 620)"/>
    <use href="#ring-segment" class="segment--grey" transform="translate(0 6) rotate(252 758 620)"/>
    <use href="#ring-segment" class="segment--red" transform="translate(0 -6) rotate(288 758 620)"/>
    <use href="#ring-segment" class="segment--charcoal" transform="translate(0 -6) rotate(324 758 620)"/>
  </g>

  <!-- hub -->
  <g class="hub">
    <line class="hub-divider" x1="492" y1="625" x2="645" y2="625"/>
    <line class="hub-divider" x1="873" y1="618" x2="1027" y2="618"/>
    <text class="hub-caption" x="756" y="546">Managing</text>
    <text class="hub-caption" x="758" y="575">Structure</text>
    <text class="hub-title" x="758" y="631">Advisory Board</text>
    <text class="hub-caption" x="756" y="688">Managing</text>
    <text class="hub-caption" x="758" y="716">Performance</text>
  </g>

  <!-- nodes -->
  <g class="node node--red">
    <rect class="node-box" x="605" y="85" width="200" height="153"/>
    <text class="node-label" x="705" y="153">Strategic</text>
    <text class="node-label" x="705" y="189">Plan</text>
  </g>
  <g class="node node--black">
    <rect class="node-box" x="845" y="152" width="198" height="151"/>
    <text class="node-label" x="942" y="203">Annual</text>
    <text class="node-label" x="942" y="239">Business</text>
    <text class="node-label" x="942" y="275">Plan</text>
  </g>
  <g class="node node--grey">
    <rect class="node-box" x="1118" y="385" width="195" height="152"/>
    <text class="node-label" x="1216" y="461">Departmental</text>
    <text class="node-label" x="1216" y="497">Plans</text>
  </g>
  <g class="node node--red">
    <rect class="node-box" x="1113" y="622" width="195" height="152"/>
    <text class="node-label" x="1211" y="656">Annual</text>
    <text class="node-label" x="1211" y="692">Performance</text>
    <text class="node-label" x="1211" y="729">Objectives &amp;</text>
    <text class="node-label" x="1211" y="765">KPIs</text>
  </g>
  <g class="node node--charcoal">
    <rect class="node-box" x="1030" y="837" width="198" height="153"/>
    <text class="node-label" x="1129" y="887">Monthly</text>
    <text class="node-label" x="1129" y="923">Performance</text>
    <text class="node-label" x="1129" y="960">Meetings</text>
  </g>
  <g class="node node--red">
    <rect class="node-box" x="697" y="992" width="200" height="152"/>
    <text class="node-label" x="795" y="1044">Individual</text>
    <text class="node-label" x="795" y="1081">Performance</text>
    <text class="node-label" x="795" y="1117">Plan</text>
  </g>
  <g class="node node--black">
    <rect class="node-box" x="457" y="969" width="199" height="152"/>
    <text class="node-label" x="556" y="1021">Individual</text>
    <text class="node-label" x="556" y="1057">Development</text>
    <text class="node-label" x="556" y="1093">Plan</text>
  </g>
  <g class="node node--grey">
    <rect class="node-box" x="222" y="695" width="199" height="152"/>
    <text class="node-label" x="321" y="766">Succesion</text>
    <text class="node-label" x="321" y="802">Plan</text>
  </g>
  <g class="node node--red">
    <rect class="node-box" x="176" y="462" width="199" height="152"/>
    <text class="node-label" x="274" y="531">Business</text>
    <text class="node-label" x="274" y="567">Reviews</text>
  </g>
  <g class="node node--charcoal">
    <rect class="node-box" x="302" y="282" width="198" height="151"/>
    <text class="node-label" x="401" y="331">Advisory</text>
    <text class="node-label" x="401" y="367">Board</text>
    <text class="node-label" x="401" y="404">Meetings</text>
  </g>
</svg>
</body>
</html>
```